Client Marketing Brocure

We require a DL brochure design / layout. KVT is an equipment finance broker that provides finance for small businesses in the following key industries
-Transport
-Construction (Yellow Goods)
-Hospitality/catering
-Fitness
The brochures will be located at dealer/seller location for prospective equipment buyers.
The brochure layout needs images and content that are editable so they can be adjusted for each of the above industries.

Front - Large image; Logo; Text area,Ph # - 1300 482 659, webb address www.kvtlending.com.au

Back - Free design basically bullet points and a slogan

```html
<!DOCTYPE html>
<html lang="en">
<head>
<meta charset="utf-8">
<title>KVT Finance – DL Brochure</title>
<link rel="stylesheet" href="https://fonts.googleapis.com/css2?family=Titillium+Web:wght@400;600;700&display=swap">
<style>
  :root {
    --orange: #f07320;
    --navy: #262d38;
    --white: #ffffff;
    --backdrop: #6a6a6a;
    --photo-office:
      radial-gradient(ellipse 60% 40% at 70% 60%, rgba(120, 40, 50, 0.45), transparent 70%),
      radial-gradient(ellipse 55% 35% at 25% 55%, rgba(60, 50, 55, 0.5), transparent 70%),
      linear-gradient(180deg, #9a5a44 0%, #a8705a 18%, #cdbfb2 36%, #6e6068 55%, #8a6a60 70%, #c9a27c 85%, #d9b995 100%);
    --photo-transport: linear-gradient(170deg, #b0803e 0%, #7d6447 55%, #5c5246 100%);
    --photo-construction: linear-gradient(160deg, #a9b447 0%, #8e9a38 60%, #7c8a36 100%);
    --photo-hospitality: linear-gradient(170deg, #5c5a56 0%, #45433f 60%, #3a3936 100%);
    --photo-fitness: linear-gradient(170deg, #7a7b7e 0%, #5e5f63 60%, #4c4d51 100%);
  }
  * { box-sizing: border-box; margin: 0; padding: 0; }
  html, body { width: 1200px; height: 1070px; overflow: hidden; }
  body {
    background: var(--backdrop);
    font-family: "Titillium Web", Arial, sans-serif;
    position: relative;
  }
  .panel {
    position: absolute;
    width: 445px;
    height: 890px;
    background: var(--white);
    overflow: hidden;
  }
  .panel--front { left: 105px; top: 109px; }
  .panel--back { left: 617px; top: 105px; }

  /* Front */
  .hero {
    position: absolute; left: 0; top: 0; width: 100%; height: 562px;
    background: var(--photo-office);
  }
  .brand {
    position: absolute; left: 112px; top: 494px;
    display: flex; align-items: center; gap: 10px;
  }
  .brand__square { width: 40px; height: 40px; background: var(--orange); }
  .brand__name {
    font-size: 29px; font-weight: 600; color: var(--navy);
    letter-spacing: 2px; line-height: 1; white-space: nowrap;
  }
  .headline {
    position: absolute; left: 0; top: 562px; width: 100%; height: 140px;
    background: var(--orange); color: var(--white);
    text-align: center; text-transform: uppercase; font-weight: 700;
    padding-top: 20px; line-height: 1.05;
  }
  .headline__line1 { font-size: 52px; display: block; }
  .headline__line2 { font-size: 35px; display: block; margin-top: 2px; }
  .strapline {
    position: absolute; left: 0; top: 702px; width: 100%; height: 57px;
    background: var(--navy); color: var(--white);
    font-size: 22px; text-align: center; line-height: 57px;
  }
  .front-contact { position: absolute; left: 0; top: 759px; width: 100%; height: 131px; text-align: center; }
  .phone { font-weight: 700; color: var(--orange); }
  .front-contact .phone { font-size: 54px; line-height: 1; display: block; margin-top: 20px; }
  .front-contact .rule {
    width: 350px; height: 2px; margin: 8px auto 0;
    background: linear-gradient(90deg, transparent, var(--orange) 20%, var(--orange) 80%, transparent);
  }
  .web { font-size: 22px; color: var(--navy); }
  .web b { font-weight: 700; }
  .front-contact .web { display: block; margin-top: 6px; }

  /* Back */
  .services-title {
    position: absolute; left: 0; top: 0; width: 100%; height: 68px;
    text-align: center; line-height: 68px;
    font-size: 31px; font-weight: 700; color: var(--navy);
  }
  .services-title span { color: var(--orange); }
  .service-grid {
    position: absolute; left: 0; top: 68px; width: 100%; height: 532px;
  }
  .service {
    position: absolute;
    display: flex; flex-direction: column; align-items: center; justify-content: center;
    color: var(--white); font-size: 18px; text-align: center; line-height: 1.2;
  }
  .service::after {
    content: ""; position: absolute; inset: 5px;
    border: 2px solid rgba(255,255,255,0.75); border-radius: 6px;
  }
  .service--transport { left: 0; top: 0; width: 222px; height: 268px; background: var(--photo-transport); }
  .service--construction { left: 222px; top: 0; width: 223px; height: 268px; background: var(--photo-construction); }
  .service--hospitality { left: 0; top: 268px; width: 222px; height: 264px; background: var(--photo-hospitality); }
  .service--fitness { left: 222px; top: 268px; width: 223px; height: 264px; background: var(--photo-fitness); }
  .service__icon {
    width: 52px; height: 52px; background: var(--white);
    border: 3px solid var(--orange); border-radius: 6px;
    display: flex; align-items: center; justify-content: center;
    margin-bottom: 8px;
  }
  .service__icon svg { width: 32px; height: 32px; }
  .grid-badge {
    position: absolute; left: 185px; top: 230px; width: 76px; height: 76px;
    background: var(--orange); border: 3px solid var(--white); border-radius: 12px;
    z-index: 2;
  }
  .slogan { position: absolute; left: 0; top: 600px; width: 100%; height: 164px; text-align: center; color: var(--navy); }
  .slogan__lead { display: block; font-size: 27px; font-weight: 700; margin-top: 18px; line-height: 1; }
  .slogan__main { display: block; font-size: 54px; font-weight: 700; line-height: 1; margin-top: 4px; }
  .slogan__sub { display: block; font-size: 22px; margin-top: 6px; }
  .back-phone {
    position: absolute; left: 0; top: 764px; width: 100%; height: 80px;
    background: var(--orange); text-align: center;
  }
  .back-phone .phone { color: var(--white); font-size: 54px; line-height: 80px; }
  .back-web {
    position: absolute; left: 0; top: 844px; width: 100%; height: 46px;
    background: var(--navy); text-align: center; line-height: 46px;
  }
  .back-web .web { color: var(--white); }
</style>
</head>
<body>

<section class="panel panel--front">
  <div class="hero" role="img" aria-label="Photo of a smiling team of businesswomen working together at a wooden office desk with laptops, brick wall and shelves behind"></div>
  <div class="brand">
    <span class="brand__square"></span>
    <span class="brand__name">KVT FINANCE</span>
  </div>
  <h1 class="headline">
    <span class="headline__line1">Starting and</span>
    <span class="headline__line2">Growing a Business</span>
  </h1>
  <p class="strapline">Team up with industry specialists</p>
  <div class="front-contact">
    <span class="phone">1300 482 659</span>
    <div class="rule"></div>
    <span class="web">www.<b>kvtlending</b>.com.au</span>
  </div>
</section>

<section class="panel panel--back">
  <h2 class="services-title">WE <span>SERVICE</span></h2>
  <div class="service-grid">
    <div class="service service--transport" role="img" aria-label="Photo of a truck on a highway at sunset">
      <div class="service__icon">
        <svg viewBox="0 0 32 32"><path fill="#262d38" d="M3 9h16v13H3zM19 13h6l4 5v4H19z"/><circle cx="9" cy="23" r="3" fill="#262d38" stroke="#fff" stroke-width="1.5"/><circle cx="24" cy="23" r="3" fill="#262d38" stroke="#fff" stroke-width="1.5"/><path fill="#fff" d="M21 15h3.5l2.5 3h-6z"/></svg>
      </div>
      TRANSPORT
    </div>
    <div class="service service--construction" role="img" aria-label="Photo of a construction worker in hi-vis gear">
      <div class="service__icon">
        <svg viewBox="0 0 32 32"><rect x="8" y="4" width="16" height="25" fill="#262d38"/><g fill="#fff"><rect x="11" y="7" width="3" height="3"/><rect x="18" y="7" width="3" height="3"/><rect x="11" y="13" width="3" height="3"/><rect x="18" y="13" width="3" height="3"/><rect x="11" y="19" width="3" height="3"/><rect x="18" y="19" width="3" height="3"/><rect x="14" y="24" width="4" height="5"/></g></svg>
      </div>
      CONSTRUCTION
    </div>
    <div class="service service--hospitality" role="img" aria-label="Photo of a waiter in an apron inside a cafe">
      <div class="service__icon">
        <svg viewBox="0 0 32 32"><path fill="#262d38" d="M6 5h20L17 16v9h5v2H10v-2h5v-9z"/></svg>
      </div>
      HOSPITALITY<br>/CATERING
    </div>
    <div class="service service--fitness" role="img" aria-label="Photo of a woman lifting a barbell in a gym">
      <div class="service__icon">
        <svg viewBox="0 0 32 32"><path fill="#262d38" d="M16 28 4.5 16.5A6.5 6.5 0 0 1 16 8a6.5 6.5 0 0 1 11.5 8.5z"/><polyline points="5,16 11,16 13,12 16,21 18,14 20,16 27,16" fill="none" stroke="#fff" stroke-width="1.8" stroke-linejoin="round"/></svg>
      </div>
      FITNESS
    </div>
    <div class="grid-badge"></div>
  </div>
  <div class="slogan">
    <span class="slogan__lead">YOUR-VISION YOUR-FUTURE</span>
    <span class="slogan__main">YOUR SUCCESS</span>
    <span class="slogan__sub">We help you achieve it !</span>
  </div>
  <div class="back-phone"><span class="phone">1300 482 659</span></div>
  <div class="back-web"><span class="web">www.<b>kvtlending</b>.com.au</span></div>
</section>

</body>
</html>
```